Brightfold Sky Advisors needs a wordpress design

New consulting company based in San Francisco focusing on leading businesses (primarily startups) into the cloud. Services include: cloud architecture, security, automation, back-end design, Infrastructure Optimization, Capacity Planning. Even though we are a new company, I'd like to convey a sense of confidence to the prospective client. Logos are attached

Target Market(s)

Start-ups looking to move their application into the cloud

Industry/Entity Type

Information Technology

```html
<!DOCTYPE html>
<html lang="en">
<head>
<meta charset="utf-8">
<title>Brightfold Sky Advisors</title>
<link href="https://fonts.googleapis.com/css2?family=Open+Sans:wght@400;600;700&family=Raleway:wght@300;400;500;600&display=swap" rel="stylesheet">
<style>
:root{
  --blue:#2b8fd8;
  --blue-dark:#1f6fae;
  --ink:#2e3a44;
  --muted:#6f7a82;
  --line:#e3e8ec;
  --band:#0e2233;
  --footer:#1b2a36;
  --footer-deep:#121d26;
  --white:#ffffff;
  --soft:#f4f7f9;
}
*{box-sizing:border-box;margin:0;padding:0}
html,body{width:764px;height:1200px;overflow:hidden;background:var(--white)}
body{font-family:"Open Sans",Arial,sans-serif;color:var(--ink);font-size:8px;line-height:1.45}
.page{width:764px;height:1200px;position:relative;overflow:hidden}

/* header */
.site-header{height:62px;display:flex;align-items:center;justify-content:space-between;padding:0 34px 0 40px;background:var(--white);border-bottom:1px solid var(--line)}
.brand{display:flex;align-items:center;gap:8px}
.brand-mark{width:22px;height:22px;background:var(--blue);border-radius:50%}
.brand-name{font-family:"Raleway",sans-serif;font-weight:600;font-size:14px;color:var(--blue-dark)}
.main-nav{display:flex;gap:4px}
.main-nav a{font-family:"Raleway",sans-serif;font-size:9.5px;color:var(--ink);text-decoration:none;padding:8px 12px}
.main-nav a.active{background:var(--blue);color:var(--white)}

/* hero */
.hero{height:238px;position:relative;background:linear-gradient(180deg,#6fa9d8 0%,#9cc3e2 38%,#4b7fae 64%,#1e4f7d 100%)}
.hero-caption{position:absolute;left:0;right:0;top:82px;text-align:center;color:var(--white);font-family:"Raleway",sans-serif;font-size:17px;font-weight:500;letter-spacing:.4px;line-height:1.35;text-transform:uppercase}

/* services */
.section-title{font-family:"Raleway",sans-serif;font-weight:400;text-align:center;color:var(--blue);font-size:17px;letter-spacing:1px}
.services{padding:18px 40px 0;height:300px}
.services-grid{display:grid;grid-template-columns:repeat(3,1fr);column-gap:36px;row-gap:22px;margin-top:14px}
.service{display:flex;gap:9px}
.service-icon{flex:0 0 20px;height:20px}
.service h3{font-family:"Raleway",sans-serif;font-size:11px;font-weight:500;color:var(--ink);margin-bottom:4px}
.service p{font-size:7px;color:var(--muted);line-height:1.5;margin-bottom:7px}
.btn{display:inline-block;background:var(--blue);color:var(--white);font-size:7px;font-weight:600;padding:4px 9px;text-decoration:none}

/* projects */
.projects{height:206px;background:linear-gradient(180deg,#12293d,#0b1a27);position:relative;padding-top:14px}
.projects .section-title{color:var(--white);font-size:15px}
.slider-arrows{position:absolute;right:30px;top:18px;display:flex;gap:3px}
.slider-arrows span{width:12px;height:12px;background:var(--blue);display:flex;align-items:center;justify-content:center}
.project-row{display:flex;justify-content:center;gap:8px;margin-top:18px}
.project{width:126px;background:var(--white);padding:4px}
.project-photo{height:100px}
.project-label{text-align:center;font-size:8.5px;font-family:"Raleway",sans-serif;color:var(--ink);padding:6px 0 3px;background:#dfe6ec;margin-top:4px}

/* welcome */
.welcome{height:160px;display:flex;gap:26px;padding:18px 40px 0}
.welcome-text{flex:1}
.welcome h2{font-family:"Raleway",sans-serif;font-weight:400;font-size:17px;color:var(--ink);margin-bottom:10px}
.welcome p{font-size:7px;color:var(--muted);line-height:1.65;margin-bottom:10px}
.welcome-screen{width:270px;height:130px;border-radius:4px;background:linear-gradient(180deg,#2a2f35 0%,#4c5661 12%,#dfe6ee 13%,#f3f6f9 60%,#cfd9e3 100%)}

/* clients */
.clients{height:110px;background:var(--soft);padding-top:14px;border-top:1px solid var(--line)}
.clients .section-title{color:var(--ink);font-size:16px}
.client-row{display:flex;justify-content:space-between;align-items:center;padding:24px 44px 0}
.client{font-family:"Open Sans",sans-serif;font-weight:700;font-size:11px;color:#4a5661;display:flex;align-items:center;gap:5px}
.client i{width:9px;height:9px;background:#9aa6b0;border-radius:50%;display:inline-block}

/* footer */
.site-footer{height:104px;background:var(--footer);display:grid;grid-template-columns:1fr 1fr 1.3fr 1fr;gap:20px;padding:14px 40px 0;color:#b9c4cd}
.site-footer h4{font-family:"Raleway",sans-serif;font-weight:500;font-size:10px;color:var(--blue);margin-bottom:6px}
.site-footer li{list-style:none;font-size:7px;line-height:1.6}
.site-footer p{font-size:7px;line-height:1.55}
.social{display:flex;gap:4px}
.social span{width:11px;height:11px;background:#5d6d7a;display:block}
.signup{display:flex;margin-top:6px}
.signup span{flex:1;background:var(--white);color:#99a3ab;font-size:7px;padding:4px 5px}
.signup b{background:var(--blue);color:var(--white);font-size:7px;padding:4px 8px;font-weight:600}
.copyright{height:18px;background:var(--footer-deep);color:#8795a1;font-size:6.5px;text-align:center;line-height:18px}
</style>
</head>
<body>
<div class="page">

<header class="site-header">
  <div class="brand"><span class="brand-mark"></span><span class="brand-name">Brightfold Sky Advisors</span></div>
  <nav class="main-nav">
    <a class="active" href="#">Home</a><a href="#">About</a><a href="#">Services</a><a href="#">Projects</a><a href="#">Contact</a>
  </nav>
</header>

<section class="hero" role="img" aria-label="San Francisco city skyline by the bay under a blue sky">
  <h1 class="hero-caption">Sed ut perspiciatis unde omnis istes err sit vol<br>loremque laudantium, totam rem aperiam</h1>
</section>

<section class="services">
  <h2 class="section-title">WHAT WE DO</h2>
  <div class="services-grid">
    <div class="service">
      <svg class="service-icon" viewBox="0 0 20 20"><path d="M5 15h10a3.5 3.5 0 0 0 0-7 5 5 0 0 0-9.5 1.5A2.8 2.8 0 0 0 5 15z" fill="#2b8fd8"/></svg>
      <div><h3>Cloud Architecture</h3><p>We plan resilient cloud platforms that scale with your product, from the first launch to millions of active users.</p><a class="btn" href="#">Read More</a></div>
    </div>
    <div class="service">
      <svg class="service-icon" viewBox="0 0 20 20"><rect x="4" y="9" width="12" height="9" rx="1" fill="#2b8fd8"/><path d="M6.5 9V6.5a3.5 3.5 0 0 1 7 0V9" stroke="#2b8fd8" stroke-width="2" fill="none"/></svg>
      <div><h3>Security</h3><p>Layered protection, access control and audits keep your data and your customers safe across every environment you run.</p><a class="btn" href="#">Read More</a></div>
    </div>
    <div class="service">
      <svg class="service-icon" viewBox="0 0 20 20"><circle cx="10" cy="10" r="6" fill="none" stroke="#2b8fd8" stroke-width="3" stroke-dasharray="3 1.7"/><circle cx="10" cy="10" r="2" fill="#2b8fd8"/></svg>
      <div><h3>Automation</h3><p>Repeatable pipelines and scripted infrastructure remove manual steps so your team ships faster with fewer surprises.</p><a class="btn" href="#">Read More</a></div>
    </div>
    <div class="service">
      <svg class="service-icon" viewBox="0 0 20 20"><path d="M7 5 2 10l5 5M13 5l5 5-5 5" stroke="#2b8fd8" stroke-width="2.2" fill="none"/></svg>
      <div><h3>Back-End Design</h3><p>Clean services, sound data models and clear interfaces give your application a back end built to last.</p><a class="btn" href="#">Read More</a></div>
    </div>
    <div class="service">
      <svg class="service-icon" viewBox="0 0 20 20"><rect x="3" y="3" width="14" height="5" fill="#2b8fd8"/><rect x="3" y="11" width="14" height="5" fill="#2b8fd8"/></svg>
      <div><h3>Infrastructure Optimisation</h3><p>We tune servers, storage and networking to cut waste, lower monthly bills and lift performance where it counts.</p><a class="btn" href="#">Read More</a></div>
    </div>
    <div class="service">
      <svg class="service-icon" viewBox="0 0 20 20"><rect x="3" y="11" width="3" height="6" fill="#2b8fd8"/><rect x="8.5" y="7" width="3" height="10" fill="#2b8fd8"/><rect x="14" y="3" width="3" height="14" fill="#2b8fd8"/></svg>
      <div><h3>Capacity Planning</h3><p>Forecasts based on real usage help you grow with confidence and stay ready for the next traffic spike.</p><a class="btn" href="#">Read More</a></div>
    </div>
  </div>
</section>

<section class="projects">
  <h2 class="section-title">Recent Projects</h2>
  <div class="slider-arrows">
    <span><svg width="6" height="6" viewBox="0 0 6 6"><path d="M4 0 1 3l3 3" stroke="#fff" fill="none"/></svg></span>
    <span><svg width="6" height="6" viewBox="0 0 6 6"><path d="M2 0l3 3-3 3" stroke="#fff" fill="none"/></svg></span>
  </div>
  <div class="project-row">
    <div class="project"><div class="project-photo" role="img" aria-label="Server racks in a data centre" style="background:linear-gradient(135deg,#3a6f95,#a9c6da)"></div><div class="project-label">Perspiciatis Unde</div></div>
    <div class="project"><div class="project-photo" role="img" aria-label="Engineer working at a laptop" style="background:linear-gradient(135deg,#1d4f7e,#6ea0c8)"></div><div class="project-label">Perspiciatis Unde</div></div>
    <div class="project"><div class="project-photo" role="img" aria-label="Blue network connection graphic" style="background:linear-gradient(135deg,#0d5fa8,#57b2ea)"></div><div class="project-label">Perspiciatis Unde</div></div>
    <div class="project"><div class="project-photo" role="img" aria-label="Glowing digital cloud graphic" style="background:linear-gradient(135deg,#123a66,#4d8fd0)"></div><div class="project-label">Perspiciatis Unde</div></div>
    <div class="project"><div class="project-photo" role="img" aria-label="Row of lit server cabinets" style="background:linear-gradient(135deg,#21445f,#8db4d2)"></div><div class="project-label">Perspiciatis Unde</div></div>
  </div>
</section>

<section class="welcome">
  <div class="welcome-text">
    <h2>Welcome to Brightfold</h2>
    <p>Brightfold Sky Advisors helps young companies move their applications into the cloud with confidence. Our engineers have guided startups through migrations, rebuilds and rapid growth. We listen first, design a clear plan, then work alongside your team until the platform runs smoothly and costs stay under control. Every engagement ends with documentation your people can own.</p>
    <a class="btn" href="#">Read More</a>
  </div>
  <div class="welcome-screen" role="img" aria-label="Desktop monitor showing the company website"></div>
</section>

<section class="clients">
  <h2 class="section-title">Our Clients</h2>
  <div class="client-row">
    <span class="client"><i></i>Larkmere</span>
    <span class="client">Veltrano</span>
    <span class="client">Orvane</span>
    <span class="client"><i></i>Pellix</span>
    <span class="client">Halden Power</span>
    <span class="client">Norbay</span>
  </div>
</section>

<footer class="site-footer">
  <div><h4>Navigation</h4><ul><li>Home</li><li>About</li><li>Services</li><li>Projects</li><li>Contact</li></ul></div>
  <div><h4>Social</h4><div class="social"><span></span><span></span><span></span><span></span><span></span></div></div>
  <div><h4>Stay updated</h4><p>Subscribe to our newsletter for cloud tips and company news.</p><div class="signup"><span>Email address</span><b>Sign Up</b></div></div>
  <div><h4>Contact us</h4><p>Brightfold Sky Advisors<br>Market Street, San Francisco<br>Phone: 415 555 0142<br>hello@brightfoldsky.com</p></div>
</footer>
<div class="copyright">Copyright 2015. All Rights Reserved</div>

</div>
</body>
</html>
```